Velmora Brightstead Website

Create website for Legal Management Company which specializes in Law Office Spersriinal Management
System implementation & Training
Global presence
Paralegal Services - Remote or In-Office
Legal Research
- Judge Motion Ruling History
- Opposing Counsel Opposition Research - Historical Filings - Pattern identification
Service by Mail - Ex- Parte Notice

Probate -Heir Finder - Asset Location -

```html
<!DOCTYPE html>
<html lang="en">
<head>
<meta charset="UTF-8">
<title>Velmora Brightstead — Legal Management</title>
<link rel="stylesheet" href="https://fonts.googleapis.com/css2?family=Domine:wght@700&family=Lato:ital,wght@0,400;0,700;1,400&display=swap">
<style>
:root{
  --navy:#1c3461;
  --navy-deep:#152a52;
  --gold:#c9a04d;
  --ink:#1f2a3d;
  --text:#4a4f5a;
  --soft:#eef1f7;
  --line:#e3e6ec;
  --white:#ffffff;
}
*{box-sizing:border-box;margin:0;padding:0}
html,body{width:1200px;height:3790px;overflow:hidden}
body{position:relative;background:var(--white);font-family:"Lato",sans-serif;color:var(--text)}
.serif{font-family:"Domine",serif;font-weight:700}
.gold{color:var(--gold)}
.abs{position:absolute}
.btn{position:absolute;background:var(--gold);color:var(--white);font-weight:700;font-size:16px;border-radius:4px;display:flex;align-items:center;justify-content:center}
.underline{position:absolute;height:12px}

/* top bar & header */
.topbar{position:absolute;left:272px;top:0;width:928px;height:32px;background:var(--navy);color:var(--white);font-size:13px;display:flex;align-items:center;padding-left:40px;gap:12px}
.topbar .item{display:flex;align-items:center;gap:8px;margin-right:38px}
.topbar .socials{margin-left:auto;margin-right:90px;display:flex;gap:10px}
.topbar .socials span{width:20px;height:20px;border-radius:50%;background:var(--white)}
.brand{position:absolute;left:110px;top:42px;display:flex;align-items:center;gap:8px}
.brand .mark{width:22px;height:22px;border-radius:50%;background:var(--gold)}
.brand .name{font-family:"Lato",sans-serif;font-weight:700;font-size:20px;color:var(--navy)}
.nav{position:absolute;left:434px;top:66px;display:flex;gap:25px;font-size:14.5px;color:var(--ink)}
.nav .active{color:var(--gold);text-decoration:underline}
.header-cta{left:954px;top:53px;width:134px;height:47px;font-size:17px}

/* hero */
.hero{position:absolute;left:0;top:120px;width:1200px;height:630px;overflow:hidden}
.hero-photo{position:absolute;left:0;top:0;width:1200px;height:630px;background:linear-gradient(90deg,#f7f6f3 0%,#f3f1ec 38%,#d9d6d0 55%,#8a8f98 72%,#4b5566 100%)}
.hero h1{position:absolute;left:112px;top:98px;font-size:54px;line-height:65px;color:var(--navy)}
.hero p{position:absolute;left:112px;top:316px;width:380px;font-size:16px;line-height:26px;color:var(--ink)}
.hero .btn{left:112px;top:412px;width:231px;height:48px}
.hero-wave{position:absolute;left:0;top:690px;width:1200px;height:70px}

/* about */
.about-frame{position:absolute;left:107px;top:826px;width:446px;height:390px;border:2px solid var(--gold);border-radius:6px}
.about-photo{position:absolute;left:118px;top:837px;width:441px;height:381px;background:linear-gradient(135deg,#c7b8a6,#8e7f70 45%,#d8d5cf);border-radius:4px}
.about h2{position:absolute;left:641px;top:822px;font-size:40px;color:var(--navy)}
.about .text{position:absolute;left:641px;top:906px;width:447px;height:240px;overflow:hidden;font-size:14.6px;line-height:25.7px;text-align:justify;color:var(--text)}
.about .text p{margin-bottom:8px}
.about .btn{left:643px;top:1171px;width:134px;height:47px}

/* services */
.services{position:absolute;left:0;top:1303px;width:1200px;height:530px;background:var(--soft)}
.section-title{position:absolute;left:0;width:1200px;text-align:center;font-size:40px;color:var(--navy)}
.svc{position:absolute;top:167px;width:231px;height:274px;background:var(--white);border-radius:8px;border-bottom:5px solid var(--gold);box-shadow:0 2px 8px rgba(0,0,0,.06)}
.svc .icon{position:absolute;left:17px;top:12px;width:85px;height:85px;border-radius:50%;background:var(--navy-deep);display:flex;align-items:center;justify-content:center}
.svc .go{position:absolute;right:-4px;top:-4px;width:42px;height:42px;border-radius:50%;background:var(--white);box-shadow:0 1px 6px rgba(0,0,0,.12);display:flex;align-items:center;justify-content:center}
.svc h3{position:absolute;left:17px;top:115px;width:200px;font-size:17px;line-height:25px;color:var(--ink);font-weight:700}
.svc p{position:absolute;left:17px;top:160px;width:205px;height:69px;overflow:hidden;font-size:14px;line-height:23px;color:var(--text)}
.svc p.short{top:180px;height:46px}
.svc a,.why a{position:absolute;font-size:13px;font-style:italic;color:var(--text);text-decoration:underline}
.svc a{left:19px;top:235px}

/* why */
.why{position:absolute;width:305px;height:198px;background:var(--white);border:1px solid var(--line);border-radius:6px;box-shadow:0 2px 6px rgba(0,0,0,.08)}
.why svg{position:absolute;left:18px;top:18px}
.why h3{position:absolute;left:18px;top:78px;font-size:19px;font-weight:400;color:var(--ink)}
.why p{position:absolute;left:18px;top:114px;width:260px;height:50px;overflow:hidden;font-size:13.5px;line-height:25px;color:var(--text)}
.why a{left:20px;top:170px;font-size:12.5px}

/* cta */
.cta{position:absolute;left:0;top:2490px;width:1200px;height:390px}
.cta h2{position:absolute;left:0;top:86px;width:1200px;text-align:center;color:var(--white);font-size:42px}
.cta p{position:absolute;left:150px;top:173px;width:900px;text-align:center;color:var(--white);font-size:16.5px;line-height:26px}
.cta .btn{left:485px;top:253px;width:231px;height:47px;font-size:17px}

/* testimonials */
.quote{position:absolute;top:3044px;width:310px;height:258px;background:var(--white);border:1px solid var(--line);border-radius:10px;box-shadow:0 2px 8px rgba(0,0,0,.08)}
.quote .stars{position:absolute;left:24px;top:20px;display:flex;gap:4px}
.quote .mark{position:absolute;right:22px;top:8px;font-family:"Domine",serif;font-size:48px;color:var(--navy)}
.quote h3{position:absolute;left:24px;top:54px;font-size:16px;font-weight:400;color:var(--ink)}
.quote p{position:absolute;left:24px;top:88px;width:265px;height:78px;overflow:hidden;font-size:14px;line-height:26px}
.quote .avatar{position:absolute;left:24px;top:178px;width:62px;height:62px;border-radius:50%;background:linear-gradient(#d8d8d8,#b6b6b6)}
.quote .who{position:absolute;left:104px;top:186px;font-size:16px;color:var(--ink);font-weight:700}
.quote .role{position:absolute;left:104px;top:214px;font-size:14px}
.arrow{position:absolute;top:3158px;font-size:40px;color:var(--navy);font-weight:700}

/* footer */
.footer{position:absolute;left:0;top:3380px;width:1200px;height:410px}
.footer .brand-f{position:absolute;left:110px;top:152px;display:flex;align-items:center;gap:10px}
.footer .brand-f span:first-child{width:24px;height:24px;border-radius:50%;background:var(--white)}
.footer .brand-f span:last-child{font-weight:700;font-size:21px;color:var(--white)}
.footer .blurb{position:absolute;left:110px;top:252px;width:220px;font-size:14.5px;line-height:25.5px;color:var(--white)}
.fcol{position:absolute;top:98px;color:var(--white)}
.fcol h4{font-size:16px;font-weight:400;margin-bottom:14px}
.fcol ul{list-style:none}
.fcol li{font-size:14px;height:34.3px;display:flex;align-items:flex-start;gap:14px}
.fcol li::before{content:"";width:8px;height:8px;border-radius:50%;background:var(--white);margin-top:5px}
.fcontact{position:absolute;left:862px;top:98px;color:var(--white);font-size:14px;line-height:25px}
.fcontact h4{font-size:16px;font-weight:400;margin-bottom:8px}
.fcontact .row{display:flex;gap:10px;margin-bottom:16px}
.fline{position:absolute;left:110px;top:345px;width:978px;height:1px;background:rgba(255,255,255,.35)}
.fsocial{position:absolute;left:112px;top:358px;display:flex;gap:10px}
.fsocial span{width:21px;height:21px;border-radius:50%;background:var(--white)}
.copy{position:absolute;right:112px;top:362px;color:var(--white);font-size:14px}
</style>
</head>
<body>

<div class="topbar">
  <div class="item">
    <svg width="16" height="12" viewBox="0 0 16 12"><rect x="1" y="1" width="14" height="10" fill="none" stroke="#fff" stroke-width="1.5"/><path d="M1 1l7 6 7-6" fill="none" stroke="#fff" stroke-width="1.5"/></svg>
    hello@velmorabrightstead.com
  </div>
  <div class="item">
    <svg width="12" height="16" viewBox="0 0 12 16"><path d="M6 15C2 10 1 8 1 6a5 5 0 0 1 10 0c0 2-1 4-5 9z" fill="#fff"/><circle cx="6" cy="6" r="2" fill="#1c3461"/></svg>
    218 Harlow Avenue, Suite 4, Brookvale, NY 10462
  </div>
  <div class="socials"><span></span><span></span><span></span><span></span></div>
</div>
<div class="brand"><span class="mark"></span><span class="name">Velmora Brightstead</span></div>
<nav class="nav">
  <span class="active">Home</span><span>About Us</span><span>Services</span><span>Legal Research</span><span>Global Presence</span>
</nav>
<div class="btn header-cta">Contact Us</div>

<section class="hero">
  <div class="hero-photo" role="img" aria-label="Two legal professionals reviewing documents at a laptop in a bright office"></div>
  <h1 class="serif">Prudent Legal<br><span class="gold">Management</span><br>Simplified</h1>
  <p>End-to-end law office management, paralegal services, and legal research—delivered globally with precision and discretion.</p>
  <div class="btn">Request a Consultation</div>
</section>
<svg class="hero-wave" viewBox="0 0 1200 70" preserveAspectRatio="none">
  <path d="M0 62 Q600 -10 1200 48 L1200 70 L0 70 Z" fill="#fff"/>
  <path d="M0 62 Q600 -10 1200 48" fill="none" stroke="#1c3461" stroke-width="7"/>
</svg>

<section class="about">
  <div class="about-frame"></div>
  <div class="about-photo" role="img" aria-label="Lawyer meeting a client across a desk with papers"></div>
  <h2 class="serif">About <span class="gold">Us</span></h2>
  <svg class="underline" style="left:641px;top:874px" width="112" height="12" viewBox="0 0 112 12"><path d="M2 10 Q56 -2 110 10" fill="none" stroke="#1c3461" stroke-width="3"/></svg>
  <div class="text">
    <p>Velmora Brightstead is a legal management company dedicated to strengthening law practices through intelligent systems, skilled support, and research-driven insights. We specialize in Law Office Management System implementation and training, helping legal professionals streamline operations, improve compliance, and focus on delivering strong legal outcomes.</p>
    <p>With a global presence, we provide remote and in-office paralegal services designed to integrate seamlessly with law firms, legal departments, and solo practitioners. Our teams operate with discretion and accuracy across every engagement.</p>
  </div>
  <div class="btn">Read More</div>
</section>

<section class="services">
  <h2 class="section-title serif" style="top:68px">Our <span class="gold">Services</span></h2>
  <svg class="underline" style="left:544px;top:124px" width="112" height="12" viewBox="0 0 112 12"><path d="M2 10 Q56 -2 110 10" fill="none" stroke="#1c3461" stroke-width="3"/></svg>

  <div class="svc" style="left:112px">
    <div class="icon"><svg width="40" height="40" viewBox="0 0 40 40"><circle cx="20" cy="20" r="12" fill="none" stroke="#c9a04d" stroke-width="4" stroke-dasharray="5 3"/><circle cx="20" cy="20" r="5" fill="#c9a04d"/></svg></div>
    <div class="go"><svg width="12" height="10" viewBox="0 0 12 10"><path d="M0 5h10M6 1l4 4-4 4" fill="none" stroke="#1f2a3d" stroke-width="1.5"/></svg></div>
    <h3>System implementation &amp; Training</h3>
    <p class="short">We specialize in the implementation, customization, and training of office systems.</p>
    <a>Read More</a>
  </div>
  <div class="svc" style="left:360px">
    <div class="icon"><svg width="40" height="40" viewBox="0 0 40 40"><path d="M6 28h10l8-4h8" fill="none" stroke="#c9a04d" stroke-width="3"/><rect x="16" y="8" width="10" height="12" fill="#c9a04d"/></svg></div>
    <div class="go"><svg width="12" height="10" viewBox="0 0 12 10"><path d="M0 5h10M6 1l4 4-4 4" fill="none" stroke="#1f2a3d" stroke-width="1.5"/></svg></div>
    <h3>Paralegal Services</h3>
    <p>Our experienced paralegal professionals provide dependable support tailored to your firm.</p>
    <a>Read More</a>
  </div>
  <div class="svc" style="left:607px">
    <div class="icon"><svg width="40" height="40" viewBox="0 0 40 40"><circle cx="22" cy="16" r="9" fill="none" stroke="#c9a04d" stroke-width="3"/><path d="M15 23L6 33" stroke="#c9a04d" stroke-width="4"/></svg></div>
    <div class="go"><svg width="12" height="10" viewBox="0 0 12 10"><path d="M0 5h10M6 1l4 4-4 4" fill="none" stroke="#1f2a3d" stroke-width="1.5"/></svg></div>
    <h3>Legal Research</h3>
    <p>We deliver in-depth, actionable legal research to support litigation strategy and case planning.</p>
    <a>Read More</a>
  </div>
  <div class="svc" style="left:854px">
    <div class="icon"><svg width="40" height="40" viewBox="0 0 40 40"><rect x="9" y="7" width="18" height="25" fill="none" stroke="#c9a04d" stroke-width="3"/><path d="M13 14h10M13 20h10M13 26h6" stroke="#c9a04d" stroke-width="2"/><rect x="24" y="20" width="9" height="12" fill="#c9a04d"/></svg></div>
    <div class="go"><svg width="12" height="10" viewBox="0 0 12 10"><path d="M0 5h10M6 1l4 4-4 4" fill="none" stroke="#1f2a3d" stroke-width="1.5"/></svg></div>
    <h3>Probate</h3>
    <p>We ensure compliant and timely handling of service by mail and ex-parte notice.</p>
    <a>Read More</a>
  </div>
</section>

<h2 class="section-title serif" style="top:1900px">Why Choose <span class="gold">Velmora Brightstead</span></h2>
<svg class="underline" style="left:544px;top:1956px" width="112" height="12" viewBox="0 0 112 12"><path d="M2 10 Q56 -2 110 10" fill="none" stroke="#1c3461" stroke-width="3"/></svg>

<div class="why" style="left:110px;top:1996px">
  <svg width="48" height="44" viewBox="0 0 48 44"><circle cx="24" cy="22" r="10" fill="none" stroke="#1c3461" stroke-width="2"/><path d="M18 31l-3 11 9-4 9 4-3-11" fill="none" stroke="#1c3461" stroke-width="2"/><path d="M6 6l2 4 4 1-3 3 1 4-4-2-4 2 1-4-3-3 4-1z" fill="none" stroke="#c9a04d" stroke-width="1.5"/><path d="M40 6l2 4 4 1-3 3 1 4-4-2-4 2 1-4-3-3 4-1z" fill="none" stroke="#c9a04d" stroke-width="1.5"/></svg>
  <h3>Legal-Focused Expertise</h3>
  <p>We understand legal operations inside and out. Our services are designed for firms.</p>
  <a>Read More</a>
</div>
<div class="why" style="left:449px;top:1996px">
  <svg width="48" height="44" viewBox="0 0 48 44"><path d="M14 4a10 10 0 0 1 6 18v6h-12v-6a10 10 0 0 1 6-18z" fill="none" stroke="#1c3461" stroke-width="2"/><circle cx="30" cy="30" r="9" fill="none" stroke="#c9a04d" stroke-width="2"/><circle cx="30" cy="30" r="3" fill="#c9a04d"/></svg>
  <h3>Systems + Strategy Approach</h3>
  <p>We don't just provide support—we build structured legal management systems.</p>
  <a>Read More</a>
</div>
<div class="why" style="left:785px;top:1996px">
  <svg width="48" height="44" viewBox="0 0 48 44"><circle cx="22" cy="22" r="16" fill="none" stroke="#1c3461" stroke-width="2"/><circle cx="22" cy="22" r="9" fill="none" stroke="#c9a04d" stroke-width="2"/><path d="M22 2v40M2 22h40" stroke="#1c3461" stroke-width="1.5"/></svg>
  <h3>Global Reach, Local Precision</h3>
  <p>With a global presence, we deliver remote and in-office paralegal services worldwide.</p>
  <a>Read More</a>
</div>
<div class="why" style="left:110px;top:2219px">
  <svg width="48" height="44" viewBox="0 0 48 44"><path d="M6 2h20l8 8v30H6z" fill="none" stroke="#1c3461" stroke-width="2"/><path d="M11 14h14M11 20h14M11 26h8" stroke="#c9a04d" stroke-width="2"/><circle cx="30" cy="32" r="7" fill="#fff" stroke="#1c3461" stroke-width="2"/><path d="M35 37l6 6" stroke="#1c3461" stroke-width="2"/></svg>
  <h3>Research-Driven Advantage</h3>
  <p>Our advanced legal research—judge ruling history, opposing counsel review and more.</p>
  <a>Read More</a>
</div>
<div class="why" style="left:449px;top:2219px">
  <svg width="48" height="44" viewBox="0 0 48 44"><circle cx="18" cy="18" r="11" fill="none" stroke="#1c3461" stroke-width="2" stroke-dasharray="4 2"/><circle cx="18" cy="18" r="4" fill="#1c3461"/><circle cx="32" cy="30" r="9" fill="none" stroke="#c9a04d" stroke-width="2"/><circle cx="32" cy="30" r="3" fill="#c9a04d"/></svg>
  <h3>Specialized Probate Expertise</h3>
  <p>We offer reliable probate support, including heir identification and asset location.</p>
  <a>Read More</a>
</div>
<div class="why" style="left:785px;top:2219px">
  <svg width="48" height="44" viewBox="0 0 48 44"><path d="M20 2l16 6v12c0 10-7 18-16 22C11 38 4 30 4 20V8z" fill="none" stroke="#1c3461" stroke-width="2"/><rect x="14" y="20" width="12" height="10" fill="none" stroke="#c9a04d" stroke-width="2"/><path d="M16 20v-4a4 4 0 0 1 8 0v4" fill="none" stroke="#c9a04d" stroke-width="2"/></svg>
  <h3>Confidential &amp; Compliant</h3>
  <p>We operate with strict confidentiality protocols, secure workflows, and audits.</p>
  <a>Read More</a>
</div>

<section class="cta">
  <svg class="abs" style="left:0;top:0" width="1200" height="390" viewBox="0 0 1200 390" preserveAspectRatio="none" role="img" aria-label="Dark navy backdrop of a law library">
    <path d="M0 20 Q600 -10 1200 10 L1200 390 Q600 350 0 375 Z" fill="#1f3a68"/>
  </svg>
  <h2 class="serif">Strengthen Your Legal Operations Today</h2>
  <p>Partner with Velmora Brightstead to implement efficient legal management systems, gain research-driven insights, and access dependable paralegal support—delivered with confidentiality, precision, and global capability.</p>
  <div class="btn">Request a Consultation</div>
</section>

<h2 class="section-title serif" style="top:2942px">What Our <span class="gold">Clients Say</span></h2>
<svg class="underline" style="left:544px;top:2996px" width="112" height="12" viewBox="0 0 112 12"><path d="M2 10 Q56 -2 110 10" fill="none" stroke="#1c3461" stroke-width="3"/></svg>
<div class="arrow" style="left:34px">«</div>
<div class="arrow" style="left:1130px">»</div>

<div class="quote" style="left:112px">
  <div class="stars"><svg width="100" height="16" viewBox="0 0 100 16"><g fill="#c9a04d"><path id="st" d="M8 0l2.4 5 5.6.8-4 3.9 1 5.5L8 12.6 3 15.2l1-5.5-4-3.9 5.6-.8z"/><use href="#st" x="20"/><use href="#st" x="40"/><use href="#st" x="60"/><use href="#st" x="80"/></g></svg></div>
  <div class="mark">“</div>
  <h3>Reliable Paralegal Services</h3>
  <p>Velmora Brightstead transformed the way our firm manages cases and workflows. Their system works.</p>
  <div class="avatar" role="img" aria-label="Client portrait"></div>
  <div class="who">Clara V.,</div>
  <div class="role">Managing Partner, Law Firm</div>
</div>
<div class="quote" style="left:446px">
  <div class="stars"><svg width="100" height="16" viewBox="0 0 100 16"><g fill="#c9a04d"><use href="#st"/><use href="#st" x="20"/><use href="#st" x="40"/><use href="#st" x="60"/><use href="#st" x="80"/></g></svg></div>
  <div class="mark">“</div>
  <h3>Insightful Legal Research</h3>
  <p>The research provided—particularly judge ruling history and opposing counsel analysis—helped us prepare.</p>
  <div class="avatar" role="img" aria-label="Client portrait"></div>
  <div class="who">Noreen</div>
  <div class="role">Senior Attorney</div>
</div>
<div class="quote" style="left:779px">
  <div class="stars"><svg width="100" height="16" viewBox="0 0 100 16"><g fill="#c9a04d"><use href="#st"/><use href="#st" x="20"/><use href="#st" x="40"/><use href="#st" x="60"/><use href="#st" x="80"/></g></svg></div>
  <div class="mark">“</div>
  <h3>Trusted Probate Support Partner</h3>
  <p>“They operate like an extension of our firm. Whether we needed short-term support or long-term help.</p>
  <div class="avatar" role="img" aria-label="Client portrait"></div>
  <div class="who">Ethan Rooke</div>
  <div class="role">Legal Operations Director</div>
</div>

<footer class="footer">
  <svg class="abs" style="left:0;top:0" width="1200" height="410" viewBox="0 0 1200 410" preserveAspectRatio="none"><path d="M0 10 Q600 40 1200 0 L1200 410 L0 410 Z" fill="#1c3461"/></svg>
  <div class="brand-f"><span></span><span>Velmora Brightstead</span></div>
  <p class="blurb">Delivering structured legal operations, advanced research, and dependable paralegal</p>
  <div class="fcol" style="left:372px">
    <h4>Quick Links</h4>
    <ul><li>Home</li><li>About Us</li><li>Services</li><li>Legal Research</li><li>Probate Services</li><li>Global Presence</li></ul>
  </div>
  <div class="fcol" style="left:549px">
    <h4>Our Services</h4>
    <ul><li>Law Office Management Systems</li><li>Paralegal Services (Remote &amp; In-Office)</li><li>Legal Research &amp; Analysis</li><li>Service by Mail &amp; Ex-Parte Support</li><li>Probate Research &amp; Heir Services</li></ul>
  </div>
  <div class="fcontact">
    <h4>Contact Us</h4>
    <div class="row"><svg width="16" height="18" viewBox="0 0 16 18"><path d="M8 17C3 11 2 9 2 7a6 6 0 0 1 12 0c0 2-1 4-6 10z" fill="#fff"/><circle cx="8" cy="7" r="2.5" fill="#1c3461"/></svg><span>218 Harlow Avenue, Suite 4,<br>Brookvale, NY 10462</span></div>
    <div class="row"><svg width="16" height="18" viewBox="0 0 16 18"><circle cx="8" cy="9" r="8" fill="#fff"/><rect x="4" y="6" width="8" height="6" fill="none" stroke="#1c3461" stroke-width="1.2"/></svg><span>info@velmorabrightstead.com</span></div>
    <div class="row" style="margin-top:8px"><svg width="16" height="18" viewBox="0 0 16 18"><path d="M3 2l3 0 1.5 4-2 1.5a9 9 0 0 0 4 4L11 9.5l4 1.5v3a2 2 0 0 1-2 2A12 12 0 0 1 1 4a2 2 0 0 1 2-2z" fill="#fff"/></svg><span>+1 555 014 2290</span></div>
  </div>
  <div class="fline"></div>
  <div class="fsocial"><span></span><span></span><span></span><span></span></div>
  <div class="copy">© 2025 Velmora Brightstead. All rights reserved.</div>
</footer>

</body>
</html>
```